Coffee bag + cups: retail packaging

Our is seeking new packaging for a new coffee shop concept. As part of this we need to design new packaging for our coffee products. For this request, we are seeking design layouts for our retail bags and a cup for to-go coffee. We are working with 3 logo versions (pending final approval).

Please reference this website to see the types of coffee bag packaging options, there's a variety of bag options. We'd like the bag to be a Gusseted Bag, size 3.625 x 9.6 x 2.3125. We want a matte laminated material, not shiny.
https://www.brewlinta.com/

BAG
We'd like to see options of a black bag, blue, and kraft paper. Reference attached example.

Below is the text for our current bags, you can use that for now. I've attached example of bags that I like. We will look to you for design thoughts.

[Front]
Logo
100% Tanzanian
12oz
Dark Roast
Ground

[Back]
Amber Ridge Farms was established in 1989 by Marcus Pendleford, son of baseball legend Walter Pendleford, and his family in rural Tanzania.
Today the coffee brand is sourced exclusively from the Pendleford farm and other small scale family owned farms in Tanzania and East Africa.
This international coffee initiative is designed to bring a greater share of coffee revenues to farmers through direct trade and help develop rural communities in East Africa.

Visit us at Calvarobeans.com

[Left panel]

Brewing instructions: Lorem ipsum dolor sit amet, consectetur adipiscing elit, sed do eiusmod tempor incididunt ut labore et dolore magna aliqua.

[Right panel]

Leave blank

Cup Sleeve
[Front of sleeve]
Logo

To-go cup
[Front]
Logo

Target Market(s)

Specialty coffee lovers.

Font styles to use
Serif
Sans Serif

Colors

Designer to choose colors to be used in the design.

Requirements
Must have
• Examples of coffee bag packaging.
• Must have; logo, text, clear and elegant labeling. Simple but strong.

```html
<!DOCTYPE html>
<html lang="en">
<head>
<meta charset="utf-8">
<title>Calvaro Coffee – Dark Roast Ground bag layout</title>
<link href="https://fonts.googleapis.com/css2?family=Montserrat:wght@300;400;500;700&family=Roboto+Condensed:wght@400&family=Arvo:wght@700&display=swap" rel="stylesheet">
<style>
  :root {
    --canvas: #f4f4f4;
    --bag-black: #0d0d0d;
    --bag-black-edge: #1b1b1b;
    --band-brown: #3a1810;
    --kraft-light: #a87a52;
    --kraft-mid: #96683f;
    --kraft-dark: #7c532f;
    --label-white: #f6f6f6;
    --ink: #111111;
    --rule: #222222;
    --white: #ffffff;
    --side-text: #e9d9c6;
    --side-heading: #d9d2cb;
    --accent-gold: #e7a13c;
  }
  * { box-sizing: border-box; margin: 0; padding: 0; }
  html, body { width: 1200px; height: 694px; overflow: hidden; background: var(--canvas); }
  body { position: relative; font-family: "Montserrat", sans-serif; }

  .panel { position: absolute; top: 71px; height: 518px; overflow: hidden; }
  .panel--gusset {
    width: 158px;
    background: linear-gradient(90deg, var(--kraft-dark), var(--kraft-light) 30%, var(--kraft-mid) 70%, var(--kraft-dark));
  }
  .panel--face {
    width: 282px;
    background: linear-gradient(90deg, var(--bag-black-edge), var(--bag-black) 12%, var(--bag-black) 88%, var(--bag-black-edge));
  }
  .gusset-left { left: 78px; }
  .face-front { left: 292px; }
  .gusset-right { left: 632px; }
  .face-back { left: 841px; }

  .band { position: absolute; left: 0; right: 0; background: var(--band-brown); }
  .band--top { top: 0; height: 19px; }
  .band--bottom { bottom: 0; height: 24px; display: flex; align-items: center; justify-content: center; }
  .net-weight { font-family: "Roboto Condensed", sans-serif; font-size: 10px; color: var(--white); }

  .brand-mark {
    position: absolute; left: 0; right: 0;
    display: flex; align-items: center; justify-content: center; gap: 8px;
  }
  .brand-mark__dot { width: 12px; height: 12px; border-radius: 50%; background: var(--white); }
  .brand-mark__name {
    font-family: "Montserrat", sans-serif; font-weight: 700; font-size: 20px;
    letter-spacing: 3px; color: var(--white); text-transform: uppercase;
  }
  .face-front .brand-mark { top: 186px; }
  .face-back .brand-mark { top: 209px; }

  .product-label {
    position: absolute; left: 38px; top: 228px; width: 207px; height: 245px;
    background: linear-gradient(180deg, var(--white), var(--label-white));
    padding: 20px 19px 0 15px; color: var(--ink);
  }
  .product-label__roast { font-weight: 700; font-size: 20px; line-height: 20px; letter-spacing: 0.2px; }
  .product-label__grind { font-weight: 300; font-size: 18px; line-height: 22px; }
  .product-label__origin { font-weight: 500; font-size: 11.5px; margin-top: 10px; letter-spacing: 0.3px; }
  .product-label__rule { border: 0; border-top: 1px solid var(--rule); margin: 7px 0; }
  .roast-level { display: flex; align-items: center; font-size: 8.5px; height: 16px; }
  .roast-level__dots { display: flex; gap: 3px; margin-left: 8px; }
  .roast-level__dot { width: 8px; height: 8px; border-radius: 50%; border: 1px solid var(--ink); }
  .roast-level__dot--on { background: var(--ink); }
  .product-label__desc { font-weight: 400; font-size: 9.6px; line-height: 12.6px; }
  .product-label__fine { font-size: 7.3px; line-height: 9.6px; padding-left: 4px; margin-top: 4px; }
  .product-label__fine strong { font-weight: 700; }

  .side-copy { position: absolute; left: 12px; right: 12px; top: 228px; text-align: center; }
  .side-copy__roast { font-family: "Arvo", serif; font-weight: 700; font-size: 10px; color: var(--side-heading); letter-spacing: 0.5px; }
  .side-copy__grind { font-family: "Arvo", serif; font-weight: 700; font-size: 14px; line-height: 15px; color: var(--side-heading); letter-spacing: 0.5px; }
  .side-copy__para { font-size: 5.6px; line-height: 9.6px; color: var(--side-text); margin-top: 10px; padding: 0 20px; }

  .story-box {
    position: absolute; left: 40px; top: 254px; width: 203px; height: 219px;
    border: 1px solid var(--white); border-radius: 3px;
    padding: 11px 10px 0; text-align: center; color: var(--white);
  }
  .story-box__text { font-size: 8.4px; line-height: 13px; }
  .story-box__visit { font-family: "Roboto Condensed", sans-serif; font-size: 8px; color: var(--accent-gold); margin-top: 7px; }
  .story-box__url { font-family: "Roboto Condensed", sans-serif; font-size: 11px; letter-spacing: 0.8px; margin-top: 2px; }
</style>
</head>
<body>
  <section class="panel panel--gusset gusset-left" aria-label="Left gusset, kraft paper"></section>

  <section class="panel panel--face face-front" aria-label="Bag front">
    <div class="band band--top"></div>
    <div class="brand-mark">
      <span class="brand-mark__dot"></span>
      <span class="brand-mark__name">Calvaro Coffee</span>
    </div>
    <div class="product-label">
      <h1 class="product-label__roast">DARK ROAST</h1>
      <p class="product-label__grind">Ground</p>
      <p class="product-label__origin">100% Tanzanian</p>
      <hr class="product-label__rule">
      <div class="roast-level">roast level:
        <span class="roast-level__dots">
          <span class="roast-level__dot roast-level__dot--on"></span>
          <span class="roast-level__dot roast-level__dot--on"></span>
          <span class="roast-level__dot roast-level__dot--on"></span>
          <span class="roast-level__dot"></span>
          <span class="roast-level__dot"></span>
          <span class="roast-level__dot"></span>
        </span>
      </div>
      <hr class="product-label__rule">
      <p class="product-label__desc">This fully-washed coffee comes from the Aipe, Huila region of Colombia. Its sweet flavors and syrupy body are great with any brewing method.</p>
      <hr class="product-label__rule">
      <p class="product-label__fine">Ingredients: organic coffee<br><strong>Calvarobeans.com</strong><br>Certified Organic bt the OCTB</p>
    </div>
    <div class="band band--bottom"><span class="net-weight">Net weight: 12oz</span></div>
  </section>

  <section class="panel panel--gusset gusset-right" aria-label="Right gusset, kraft paper">
    <div class="side-copy">
      <p class="side-copy__roast">DARK ROAST</p>
      <p class="side-copy__grind">GROUND</p>
      <p class="side-copy__para">Lorem Ipsum is simply dummy text of the printing and typesetting industry. Lorem Ipsum has been the industry's standard dummy text ever since</p>
      <p class="side-copy__para">the 1500s, when an unknown printer took a galley of type and scrambled it to make a type specimen book. It has survived not only five centu</p>
      <p class="side-copy__para">ries, but also the leap into electronic typesetting, re-maining essentially un-changed. Dark Roast Ground</p>
      <p class="side-copy__para">ries, but also the leap into electronic typesetting, re-maining essentially un-changed. Dark Roast Ground</p>
    </div>
  </section>

  <section class="panel panel--face face-back" aria-label="Bag back">
    <div class="band band--top"></div>
    <div class="brand-mark">
      <span class="brand-mark__dot"></span>
      <span class="brand-mark__name">Calvaro Coffee</span>
    </div>
    <div class="story-box">
      <p class="story-box__text">Amber Ridge Farms was established in 1989 by Marcus Pendleford, son of baseball legend Walter Pendleford, and his family in rural Tanzania. Today the coffee brand is sourced exclusively from the Pendleford farm and other small scale family owned farms in Tanzania and East Africa. This international coffee initiative is designed to bring a greater share of coffee revenues to farmers through direct trade and help develop rural communities in East Africa.</p>
      <p class="story-box__visit">- Visit us at -</p>
      <p class="story-box__url">www.Calvarobeans.com</p>
    </div>
    <div class="band band--bottom"></div>
  </section>
</body>
</html>
```